Nanny Agency Needs a Newspaper Ad

We need a newspaper ad for a new company based in New York City called "Sitters by Elka". We place top sitters and nannies with families in Manhattan, The Hamptons, Brooklyn, and New Jersey. We do live-in, live-out, short term, long term, and one time jobs. Our most popular service is our saturday night sitter, where we get clients reliable sitters for saturday nights at low prices. We would like to see designs that use bright colors, like hot pink and teal. The final ad should represent our company, and should look a lot like our logo.

We are planning to put it in 'The Harbor Ledger' Magazine, so we want it to say that we have sitters who have experience with Jewish families and working in a Kosher home.

It should say that we are a nanny agency based in Manhattan, The Hamptons, New Jersey, and Brooklyn that does full time, part time, and one time placements with great screened nannies and sitters.

sittersbyelka.example

Target Market(s)

Parents

Requirements
Must have
• Logo and colors of our logo.

```html
<!DOCTYPE html>
<html lang="en">
<head>
<meta charset="utf-8">
<title>Sitters by Elka – Newspaper Ad</title>
<link href="https://fonts.googleapis.com/css2?family=Arimo:wght@400;700&display=swap" rel="stylesheet">
<style>
  :root {
    --page-bg: #ececec;
    --pink: #ec1b8c;
    --teal: #16a68f;
    --white: #ffffff;
    --ink: #000000;
    --mono-frame: #000000;
    --mono-logo: #8a8a8a;
  }
  * { box-sizing: border-box; margin: 0; padding: 0; }
  html, body { width: 1200px; height: 1000px; overflow: hidden; }
  body {
    background: var(--page-bg);
    font-family: "Arimo", Arial, sans-serif;
    position: relative;
  }
  .ad {
    position: absolute;
    top: 171px;
    width: 324px;
    height: 558px;
    background: var(--frame);
    box-shadow: 0 6px 18px rgba(0,0,0,0.25);
    --frame: var(--pink);
    --band: var(--teal);
    --headline: var(--teal);
    --logo: var(--pink);
  }
  .ad--color { left: 150px; }
  .ad--mono {
    left: 677px;
    --frame: var(--mono-frame);
    --band: var(--mono-frame);
    --headline: var(--ink);
    --logo: var(--mono-logo);
  }
  .ad__header {
    position: absolute; top: 0; left: 0; right: 0; height: 50px;
    color: var(--white); text-align: center;
  }
  .ad__title { font-weight: 700; font-size: 18.8px; padding-top: 7px; }
  .ad__areas { font-weight: 700; font-size: 12.2px; margin-top: 3px; }
  .ad__logo-box {
    position: absolute; top: 50px; left: 6px; right: 6px; height: 82px;
    background: var(--white);
    display: flex; align-items: center; justify-content: center; gap: 10px;
  }
  .ad__brand {
    font-weight: 700; font-size: 34px; color: var(--logo); letter-spacing: -0.5px;
  }
  .ad__brand-dot {
    width: 14px; height: 14px; border-radius: 50%; background: var(--logo);
  }
  .ad__services {
    position: absolute; top: 132px; left: 0; right: 0; height: 25px;
    background: var(--band); color: var(--white);
    font-weight: 700; font-size: 11.2px; text-align: center; line-height: 25px;
  }
  .ad__headline-box {
    position: absolute; top: 157px; left: 6px; right: 6px; height: 118px;
    background: var(--white); color: var(--headline);
    text-align: center; line-height: 1;
  }
  .ad__line1 { font-size: 26px; padding-top: 7px; text-transform: uppercase; }
  .ad__line2 { font-size: 31.5px; margin-top: 3px; text-transform: uppercase; }
  .ad__line3 { font-size: 22.5px; font-weight: 700; margin-top: 4px; text-transform: uppercase; }
  .ad__kosher { font-size: 11px; font-weight: 700; margin-top: 6px; }
  .ad__web {
    position: absolute; top: 275px; left: 0; right: 0; height: 30px;
    background: var(--band); color: var(--white);
    font-weight: 700; font-size: 16px; letter-spacing: 3.6px;
    text-align: center; line-height: 30px;
  }
  .ad__photo {
    position: absolute; top: 305px; left: 6px; right: 6px; height: 216px;
  }
  .ad--color .ad__photo {
    background: linear-gradient(90deg, #f4efe6 0%, #efe6d6 35%, #3b4a52 60%, #5d6f86 80%, #f7f7f7 100%);
  }
  .ad--mono .ad__photo {
    background: linear-gradient(90deg, #f2f2f2 0%, #e2e2e2 35%, #3a3a3a 60%, #6a6a6a 80%, #f7f7f7 100%);
  }
  .ad__cta {
    position: absolute; bottom: 0; left: 0; right: 0; height: 37px;
    color: var(--white); font-weight: 700; font-size: 22.5px;
    text-align: center; line-height: 37px;
  }
</style>
</head>
<body>
  <section class="ad ad--color">
    <header class="ad__header">
      <p class="ad__title">YOUR FAVORIT NANNY AGENCY</p>
      <p class="ad__areas">Manhattan - The Hamptons - Brooklyn - New Jersey</p>
    </header>
    <div class="ad__logo-box">
      <span class="ad__brand">Sitters by Elka</span>
      <span class="ad__brand-dot"></span>
    </div>
    <p class="ad__services">live-in, live-out, short term, long term, and one time jobs</p>
    <div class="ad__headline-box">
      <p class="ad__line1">For Saturday Night</p>
      <p class="ad__line2">Great Screened</p>
      <p class="ad__line3">Nannies and Sitters.</p>
      <p class="ad__kosher">Experienced with Jewish families &amp; Kosher homes</p>
    </div>
    <p class="ad__web">www.sittersbyelka.example</p>
    <div class="ad__photo" role="img" aria-label="Photo of a girl and a boy sitting on the floor playing with a spinning top and coins"></div>
    <p class="ad__cta">CALL NOW&nbsp; 0 55 01234567</p>
  </section>

  <section class="ad ad--mono">
    <header class="ad__header">
      <p class="ad__title">YOUR FAVORIT NANNY AGENCY</p>
      <p class="ad__areas">Manhattan - The Hamptons - Brooklyn - New Jersey</p>
    </header>
    <div class="ad__logo-box">
      <span class="ad__brand">Sitters by Elka</span>
      <span class="ad__brand-dot"></span>
    </div>
    <p class="ad__services">live-in, live-out, short term, long term, and one time jobs</p>
    <div class="ad__headline-box">
      <p class="ad__line1">For Saturday Night</p>
      <p class="ad__line2">Great Screened</p>
      <p class="ad__line3">Nannies and Sitters.</p>
      <p class="ad__kosher">Experienced with Jewish families &amp; Kosher homes</p>
    </div>
    <p class="ad__web">www.sittersbyelka.example</p>
    <div class="ad__photo" role="img" aria-label="Black and white photo of a girl and a boy sitting on the floor playing with a spinning top and coins"></div>
    <p class="ad__cta">CALL NOW&nbsp; 0 55 01234567</p>
  </section>
</body>
</html>
```